Motel Sign - Front

(21/03/12 - I've edited the brief and removing the words "garden view" its not fitting in the designs I'm getting and just want the word motel to be the focus. I have a template/vision of what I want - see the whiteboard sketch of what I'm looking for uploaded today. Definitely open to creatively, new designs and different ideas but the whiteboard design I've done should be a guideline. Keep it fresh/green/white. use the sample photos of green as inspiration. Thanks)
We are a motel set in the mountain country of Victoria - Australia. The front of the motel needs a fresh look. We recently removed a large amount of the garden to expose a brick courtyard fence which the front of the courtyard faces out to the main road. Within the courtyard fence there is a wooden frame and paneling.
We want to have a new sign created to slot into the wooden frame. (see photo) its the white component.
Its a very large and unusual shape and I want to keep it simple but need to fill the in the best way possible.
The space is 940mm high and 4940mm width.
The message of the sign is simple the word "MOTEL". I want people to be able to drive past and glance in and see we are a motel straight away. So the main purpose of the sign is to say "MOTEL".
I am open to colour use to match the space and have impact. I thought a background colour should be 'off white'. I'm open to the colours used to match your design as long as it matches the brief. Maybe a garden green for the emblem.
IN BRIEF:
1) the word "MOTEL"
2) Border/Background that ties in the garden.
The design should be centred, clean and simple, doesn't have to fill the whole space as long as its balanced and centred.
I like cursive and garden like designs for this one - as long its the word MOTEL still has impact. (OPEN TO NEW IDEAS)
I am also open to different ideas and suggestions if you feel you have a better way to take advantage of this space.
The sign will be 7-8 metres from the road itself.
NOTE: the photos show the space and the painted white in the space where the sign will go. The garden in front of this space will be completely cleared.

```html
<!DOCTYPE html>
<html lang="en">
<head>
<meta charset="UTF-8">
<title>Motel Sign – Front</title>
<link rel="stylesheet" href="https://fonts.googleapis.com/css2?family=Tinos:wght@700&display=swap">
<style>
  :root {
    --page-bg: #f4f6ef;
    --leaf-light: #d6f2a4;
    --leaf-mid: #b6e36c;
    --leaf-deep: #9fd24e;
    --type-top: #6cc04a;
    --type-bottom: #0f6a23;
    --type-edge: #0b4f1a;
    --type-rim: #ffffff;
  }
  html, body {
    margin: 0;
    padding: 0;
    width: 1200px;
    height: 857px;
    overflow: hidden;
    background: var(--page-bg);
  }
  .canvas {
    position: relative;
    width: 1200px;
    height: 857px;
    display: flex;
    align-items: center;
    justify-content: center;
  }
  .sign {
    position: relative;
    width: 1100px;
    height: 209px;
    box-shadow: 0 2px 0 rgba(255,255,255,0.9), 0 6px 18px rgba(30,60,20,0.18);
  }
  .sign__leaves {
    position: absolute;
    inset: 0;
    background:
      radial-gradient(ellipse 30% 70% at 12% 30%, rgba(255,255,255,0.35), transparent 70%),
      radial-gradient(ellipse 25% 60% at 88% 75%, rgba(255,255,255,0.3), transparent 70%),
      radial-gradient(ellipse 35% 80% at 55% 10%, rgba(255,255,255,0.25), transparent 70%),
      linear-gradient(100deg, var(--leaf-light) 0%, var(--leaf-mid) 45%, var(--leaf-deep) 75%, var(--leaf-mid) 100%);
  }
  .sign__word {
    position: absolute;
    inset: 0;
    width: 100%;
    height: 100%;
  }
  .sign__word text {
    font-family: "Tinos", "Times New Roman", serif;
    font-weight: 700;
    font-size: 168px;
  }
  .sign__word .word-edge {
    fill: var(--type-edge);
    stroke: var(--type-edge);
    stroke-width: 14;
    stroke-linejoin: round;
  }
  .sign__word .word-face {
    fill: url(#wordFill);
    stroke: var(--type-rim);
    stroke-width: 5;
    stroke-linejoin: round;
    paint-order: stroke fill;
  }
</style>
</head>
<body>
<main class="canvas">
  <section class="sign">
    <div class="sign__leaves" role="img" aria-label="Soft pattern of overlapping fresh green leaves"></div>
    <svg class="sign__word" viewBox="0 0 1100 209" aria-label="MOTEL">
      <defs>
        <linearGradient id="wordFill" x1="0" y1="0" x2="0" y2="1">
          <stop offset="0" stop-color="var(--type-top)"/>
          <stop offset="0.35" stop-color="#9ad65a"/>
          <stop offset="0.6" stop-color="#2f8c32"/>
          <stop offset="1" stop-color="var(--type-bottom)"/>
        </linearGradient>
      </defs>
      <text class="word-edge" x="150" y="166" textLength="800" lengthAdjust="spacing" aria-hidden="true">MOTEL</text>
      <text class="word-face" x="150" y="166" textLength="800" lengthAdjust="spacing">MOTEL</text>
    </svg>
  </section>
</main>
</body>
</html>
```